Craft oriented film company needs a Business Card design

Hi all,
We're a 2-man band film company in New Zealand called Harrow Pictures. We're good honest blokes, who are very passionate about the craft of film making. I've attached our current logo which has a bit of a crafty/artisan feel that we like. Feel free to use it - or throw the baby out with the bathwater and start again..... you never know, you might inspire a complete brand re-work.

In any case, the vibe we want to give out is that we are solid, dependable and no bullshit - but without compromising creative excellence and being in the now. We like the 'Brooklyn' artisan style of work.

Preferably single sided.

We need the standard stuff:
Name, job title, cellphone, email address and physical address (this can be smaller if you like - street, suburb, city & zip, country [if you want])

Check out our website to learn more about us: harrowpictures.example

Target Market(s)

Brand marketers and advertising agency creatives looking for video production.

Industry/Entity Type

Baby

Requirements
Should not have
• Nothing flashy or too 'futuristic', we want it to feel grounded and real. A limited colour palette is preferred.
We don't want any film reels or cameras or anything obvious like that.

```html
<!DOCTYPE html>
<html lang="en">
<head>
<meta charset="utf-8">
<title>Harrow Pictures – Business Cards</title>
<link rel="stylesheet" href="https://fonts.googleapis.com/css2?family=Gelasio:wght@400;600;700&display=swap">
<style>
  :root {
    --band-light: #c2c2c4;
    --band-mid: #9a9a9c;
    --band-dark: #858587;
    --paper: #ffffff;
    --ink: #2b2b2b;
    --badge: #141414;
    --accent-dot: #9fc7c4;
    --serif: "Gelasio", Georgia, serif;
  }
  * { margin: 0; padding: 0; box-sizing: border-box; }
  html, body { width: 928px; height: 1200px; overflow: hidden; background: var(--paper); }
  .sheet { position: relative; width: 928px; height: 1200px; font-family: var(--serif); color: var(--ink); }
  .card { position: absolute; left: 0; width: 928px; height: 530px; background: var(--paper); overflow: hidden; }
  .card--first { top: 0; }
  .card--second { top: 670px; }
  .card__shapes { position: absolute; inset: 0; }
  .card__name {
    position: absolute; left: 0; width: 452px; top: 68px; text-align: center;
    font-size: 38px; font-weight: 400; color: var(--paper); letter-spacing: 0.2px;
  }
  .card__role {
    position: absolute; left: 238px; top: 124px; font-size: 19px; color: var(--paper);
  }
  .card__role::before {
    content: ""; position: absolute; left: -23px; top: 5px; width: 17px; height: 17px;
    border-radius: 50%; background: var(--accent-dot); opacity: 0.8;
  }
  .brand {
    position: absolute; left: 657px; top: -5px; width: 244px; height: 244px;
    border-radius: 50%; background: var(--badge);
    display: flex; flex-direction: column; align-items: center; justify-content: center;
    color: var(--paper); font-weight: 700; line-height: 1.1; text-align: center;
  }
  .brand__line1 { font-size: 42px; letter-spacing: 1px; }
  .brand__line2 { font-size: 21px; letter-spacing: 4px; }
  .contact { position: absolute; top: 326px; font-size: 17px; line-height: 22px; }
  .contact--left { left: 104px; font-weight: 600; }
  .contact__phone { font-size: 18px; margin-bottom: 2px; }
  .contact--right { left: 498px; }
  .contact__email { font-size: 17px; font-weight: 600; margin-bottom: 4px; }
  .contact__address { font-size: 14px; line-height: 19px; font-weight: 600; }
</style>
</head>
<body>
<main class="sheet">

  <section class="card card--first" aria-label="Business card for Rowan Teale">
    <svg class="card__shapes" width="928" height="530" viewBox="0 0 928 530" aria-hidden="true">
      <defs>
        <radialGradient id="band-glow-1" cx="230" cy="105" r="520" gradientUnits="userSpaceOnUse">
          <stop offset="0" stop-color="var(--band-light)"/>
          <stop offset="0.55" stop-color="var(--band-mid)"/>
          <stop offset="1" stop-color="var(--band-dark)"/>
        </radialGradient>
      </defs>
      <polygon points="0,0 928,0 928,268 787,304 641,268 0,268" fill="url(#band-glow-1)"/>
      <polygon points="500,530 928,421 928,530" fill="var(--band-dark)"/>
    </svg>
    <h1 class="card__name">Rowan Teale</h1>
    <p class="card__role">Producer</p>
    <div class="brand"><span class="brand__line1">HARROW</span><span class="brand__line2">PICTURES</span></div>
    <div class="contact contact--left">
      <p class="contact__phone">(64) 21-555-018</p>
      <p>www.harrowpictures.example</p>
      <p>Arts &amp; Entertainment</p>
      <p>Broadcasting &amp; Media Production</p>
    </div>
    <div class="contact contact--right">
      <p class="contact__email">rowan@harrowpictures.example</p>
      <p class="contact__address">42 Fernleaf st, tui heights,<br>auckland, new zealand 1099</p>
    </div>
  </section>

  <section class="card card--second" aria-label="Business card for Felix Marsh">
    <svg class="card__shapes" width="928" height="530" viewBox="0 0 928 530" aria-hidden="true">
      <defs>
        <radialGradient id="band-glow-2" cx="230" cy="105" r="520" gradientUnits="userSpaceOnUse">
          <stop offset="0" stop-color="var(--band-light)"/>
          <stop offset="0.55" stop-color="var(--band-mid)"/>
          <stop offset="1" stop-color="var(--band-dark)"/>
        </radialGradient>
      </defs>
      <polygon points="0,0 928,0 928,268 787,304 641,268 0,268" fill="url(#band-glow-2)"/>
      <polygon points="500,530 928,421 928,530" fill="var(--band-dark)"/>
    </svg>
    <h1 class="card__name">Felix Marsh</h1>
    <p class="card__role">Director</p>
    <div class="brand"><span class="brand__line1">HARROW</span><span class="brand__line2">PICTURES</span></div>
    <div class="contact contact--left">
      <p class="contact__phone">(64) 21-55-3010</p>
      <p>www.harrowpictures.example</p>
      <p>Arts &amp; Entertainment</p>
      <p>Broadcasting &amp; Media Production</p>
    </div>
    <div class="contact contact--right">
      <p class="contact__email">felix@harrowpictures.example</p>
      <p class="contact__address">42 Fernleaf st, tui heights,<br>auckland, new zealand 1099</p>
    </div>
  </section>

</main>
</body>
</html>
```